Structural Engineering Firm Looking for High-Impact Lead Generation Focused Design (for B2B)

A well-established structural engineering firm in the UK wants a new website designed for them which will help them realise more business from online. Directly through the website as well as Ads and lead platforms. They need to compare favourably to competitors and have clarity. Current Site is here: http://www.quarlingpartners.example/ - you can take imagery from this site if you want to help with the design.

Target Market(s)

Homeowners, Architects, Designers, Construction Companies and Landlords

Industry/Entity Type

Professional Services

Number of Pages Required

5+ page

Font styles to use
Sans Serif

Requirements
Must have
• A Strong, Simple and Professional Design with a Focus on Lead Generation
Nice to have
• Creativity in the Detail, Clear Messaging
Should not have
• Too Much Colour, Too 'Consumer', Too Much Variation

```html
<!DOCTYPE html>
<html lang="en">
<head>
<meta charset="utf-8">
<title>About Us – Quarling Partners</title>
<link rel="stylesheet" href="https://fonts.googleapis.com/css2?family=Tenor+Sans&family=Crimson+Text&display=swap">
<style>
  :root {
    --bg: #fbf3e1;
    --ink: #141414;
    --accent: #86ecca;
    --brand: #4b524c;
    --photo-sky: #b9cde6;
    --photo-leaf: #2f4a26;
  }
  * { margin: 0; padding: 0; box-sizing: border-box; }
  html, body { width: 1200px; height: 2585px; overflow: hidden; background: var(--bg); }
  body { position: relative; font-family: "Tenor Sans", sans-serif; color: var(--ink); }
  .abs { position: absolute; }

  .brand {
    font-family: "Tenor Sans", sans-serif;
    color: var(--brand);
    line-height: 0.95;
    letter-spacing: -1px;
    white-space: nowrap;
  }
  .brand-header { left: 43px; top: 50px; font-size: 46px; }
  .brand-footer { left: 828px; top: 2036px; font-size: 46px; }

  .main-nav { left: 563px; top: 88px; display: flex; font-size: 30px; letter-spacing: -0.3px; white-space: nowrap; }
  .main-nav a { color: var(--ink); text-decoration: none; }
  .main-nav .home { margin-right: 34px; }
  .main-nav .current { color: var(--accent); text-decoration: underline; text-underline-offset: 6px; margin-right: 44px; }
  .main-nav .projects { margin-right: 30px; }

  .page-title { left: 131px; top: 254px; font-size: 46px; font-weight: 400; }

  .hero-photo {
    left: 223px; top: 370px; width: 638px; height: 493px;
    background: linear-gradient(180deg, var(--photo-sky) 0%, #9aa7a8 45%, var(--photo-leaf) 75%, #2b3340 100%);
  }

  .intro { left: 104px; top: 926px; width: 1030px; font-size: 43px; line-height: 57.6px; letter-spacing: -0.8px; }
  .intro p + p { margin-top: 57.6px; }

  .enquiry { left: 104px; top: 1936px; width: 1000px; display: flex; align-items: center; gap: 32px; }
  .enquiry-text { font-size: 26px; letter-spacing: -0.2px; }
  .enquiry-button {
    display: inline-block; padding: 14px 30px; background: var(--ink); color: var(--bg);
    font-size: 22px; letter-spacing: 1.5px; text-decoration: none; white-space: nowrap;
    border-bottom: 4px solid var(--accent);
  }

  .footer-heading { font-size: 29px; letter-spacing: 1.5px; font-weight: 400; white-space: nowrap; }
  .touch-heading { left: 133px; top: 2030px; }
  .site-heading { left: 501px; top: 2032px; }

  .contact-line { font-family: "Crimson Text", serif; font-size: 20px; display: flex; align-items: center; white-space: nowrap; }
  .contact-line svg { margin-right: 44px; }
  .phone-a { left: 67px; top: 2092px; }
  .phone-b { left: 67px; top: 2140px; }
  .email { left: 67px; top: 2190px; }
  .email svg { margin-right: 12px; }

  .address { font-family: "Crimson Text", serif; font-size: 20px; line-height: 24.5px; font-style: normal; white-space: nowrap; }
  .address-main { left: 459px; top: 2093px; }
  .address-sussex { left: 464px; top: 2192px; }

  .legal-links { left: 216px; top: 2398px; font-size: 30px; letter-spacing: 1.5px; display: flex; gap: 60px; white-space: nowrap; }
  .copyright { left: 343px; top: 2454px; font-family: "Crimson Text", serif; font-size: 22px; white-space: nowrap; }
</style>
</head>
<body>
  <header>
    <div class="abs brand brand-header">QUARLING<br>PARTNERS</div>
    <nav class="abs main-nav">
      <a class="home" href="#">Home</a>
      <a class="current" href="#">About Us</a>
      <a class="projects" href="#">Projects</a>
      <a href="#">Contact Us</a>
    </nav>
  </header>

  <main>
    <h1 class="abs page-title">About Us</h1>
    <div class="abs hero-photo" role="img" aria-label="Photograph of a modern white rendered house with timber cladding at dusk, framed by trees"></div>
    <section class="abs intro">
      <p>With over a decade of experience working in residential refurbishment and new builds, Quarling Partners strive to understand the financial and emotional investment of every project.Whether it is a commercial development, private home or complex temporary works problem. We’ve provided considered and economical structural design solutions for over 300+projects, ranging from full house refurbishments to small conversions, basement excavations and commercial developments.</p>
      <p>We work hard alongside our clients and their design professional to find cost effective and practical design solutions,and you can rely on our collaborative, approachable work ethic for every project.</p>
    </section>
    <section class="abs enquiry">
      <p class="enquiry-text">Planning a project? Speak to a structural engineer today.</p>
      <a class="enquiry-button" href="#">REQUEST A QUOTE</a>
    </section>
  </main>

  <footer>
    <h2 class="abs footer-heading touch-heading">GET IN TOUCH</h2>
    <div class="abs contact-line phone-a">
      <svg width="40" height="32" viewBox="0 0 40 32" fill="none" stroke="#141414" stroke-width="2"><path d="M12 6c-4 2-5 7-2 13s8 9 12 8l1-4-4-3-2 2c-3-1-5-4-6-7l2-2-1-5z"/><path d="M6 4c-6 6-6 18 0 24M34 4c6 6 6 18 0 24"/></svg>
      <span>+44 (0) 20 7946 0381</span>
    </div>
    <div class="abs contact-line phone-b">
      <svg width="40" height="32" viewBox="0 0 40 32" fill="none" stroke="#141414" stroke-width="2"><path d="M12 6c-4 2-5 7-2 13s8 9 12 8l1-4-4-3-2 2c-3-1-5-4-6-7l2-2-1-5z"/><path d="M6 4c-6 6-6 18 0 24M34 4c6 6 6 18 0 24"/></svg>
      <span>+44 (0) 1632 960 517</span>
    </div>
    <div class="abs contact-line email">
      <svg width="36" height="36" viewBox="0 0 36 36" fill="none" stroke="#141414" stroke-width="2.2"><circle cx="18" cy="18" r="6"/><path d="M24 12v9c0 3 5 3 6-1 2-8-4-16-12-16S4 10 4 18s6 14 14 14c4 0 7-1 9-3"/></svg>
      <span>info@quarlingpartners.example</span>
    </div>

    <h2 class="abs footer-heading site-heading">SITE ADDRESS</h2>
    <address class="abs address address-main">Unit 4 Harrow Yard Studios<br>12 Penwick Lane<br>London SE1 9XY</address>
    <address class="abs address address-sussex">Our Sussex Office is<br>Hollinford West Sussex</address>

    <div class="abs brand brand-footer">QUARLING<br>PARTNERS</div>

    <div class="abs legal-links"><span>TERMS &amp; CONDITIONS</span><span>PRIVACY POLICY</span></div>
    <p class="abs copyright">Quarling. Copyright © 2022. All rights reserved</p>
  </footer>
</body>
</html>
```